Business card design for sports medicine and athlete care clinic.

We need a bold, solid business card design for our practitioners to stand out. We treat overuse & sports-related injuries and provide post-operative rehabilitation. Our specialisations include chronic conditions, men’s health, nutrition & musculoskeletal disorders (MSDs). All brand collateral in terms of fonts, logo and colour palette to be provided.

Target Market(s)

Athletes (professional and amateur), sportspeople, predominantly male

Industry/Entity Type

Health And Wellness

Contact Information for Business Card

The front of the card should be white with dark blue text the back dark blue with white text. The logo should be top-left. The business name should be horizontal and right of the logo. The tagline should be directly below centred on the back of the card (see top-banner.png and bottom-banner.png)

Font styles to use
Sans Serif

Colors
0355a3
0293ce
3176b5
ffffff
85acd3

Requirements
Nice to have
• Diagonal and/or horizontal line elements between logo and practitioner details and/or bottom corner of card (see slide.png and tag-bg.png).

```html
<!DOCTYPE html>
<html lang="en">
<head>
<meta charset="utf-8">
<title>Northpace Athletics – Business Card</title>
<link href="https://fonts.googleapis.com/css2?family=Montserrat:wght@400;500;600;700&display=swap" rel="stylesheet">
<style>
  :root {
    --stage: #2b2b2d;
    --navy: #252b63;
    --navy-deep: #1c2148;
    --navy-text: #2a3470;
    --slate: #3d4370;
    --sky: #1a9bd7;
    --cyan: #1fb3e5;
    --blue: #0293ce;
    --grey: #55586e;
    --white: #ffffff;
  }
  * { box-sizing: border-box; margin: 0; padding: 0; }
  html, body { width: 1200px; height: 1200px; overflow: hidden; }
  body {
    background: var(--stage);
    font-family: "Montserrat", sans-serif;
    position: relative;
  }
  .card {
    position: absolute;
    left: 160px;
    width: 880px;
    height: 528px;
    overflow: hidden;
  }

  /* Front */
  .card-front { top: 60px; background: linear-gradient(110deg, #2b3270 0%, var(--navy) 55%, #222862 100%); }
  .front-figure {
    position: absolute; left: 300px; top: 0; width: 420px; height: 430px;
    background: radial-gradient(ellipse at 55% 45%, rgba(120,130,200,0.22), rgba(120,130,200,0) 70%);
  }
  .front-brand { position: absolute; left: 72px; top: 160px; display: flex; align-items: center; gap: 18px; }
  .brand-mark { width: 110px; height: 110px; border-radius: 50%; background: var(--sky); flex: none; }
  .brand-name { font-weight: 700; font-size: 52px; line-height: 1; letter-spacing: -0.5px; }
  .brand-tagline { font-weight: 500; font-size: 28px; color: var(--sky); margin-top: 10px; }
  .front-brand .brand-name { color: var(--white); }
  .front-band { position: absolute; left: 0; top: 430px; width: 100%; height: 14px; background: var(--blue); }
  .front-strip {
    position: absolute; left: 0; top: 444px; width: 100%; height: 84px; background: var(--white);
    display: flex; align-items: center; justify-content: center;
    font-size: 20px; color: var(--navy-text);
  }

  /* Back */
  .card-back { top: 612px; background: var(--white); }
  .back-shapes { position: absolute; left: 0; top: 0; width: 880px; height: 528px; }
  .back-brand { position: absolute; left: 206px; top: 36px; display: flex; align-items: center; gap: 16px; }
  .back-brand .brand-mark { width: 100px; height: 100px; }
  .back-brand .brand-name { color: var(--slate); font-size: 50px; }
  .back-brand .brand-tagline { color: var(--sky); font-size: 27px; }
  .person { position: absolute; right: 32px; top: 186px; text-align: right; }
  .person-name { font-weight: 700; font-size: 31px; color: var(--navy-text); }
  .person-role { font-size: 20px; color: var(--grey); margin-top: 2px; }
  .address { position: absolute; right: 32px; top: 284px; text-align: right; font-size: 19px; line-height: 26px; color: var(--grey); }
  .contacts { position: absolute; right: 32px; top: 374px; list-style: none; }
  .contacts li { display: flex; justify-content: flex-end; align-items: center; gap: 16px; height: 39px; font-size: 19px; color: var(--grey); }
  .contact-icon { width: 30px; height: 30px; border-radius: 5px; background: var(--navy-text); display: flex; align-items: center; justify-content: center; }
</style>
</head>
<body>

<section class="card card-front">
  <div class="front-figure" role="img" aria-label="Faint brand runner decoration"></div>
  <div class="front-brand">
    <span class="brand-mark" aria-hidden="true"></span>
    <div>
      <div class="brand-name">Northpace Athletics</div>
      <div class="brand-tagline">Sports Medicine And Athlete Care</div>
    </div>
  </div>
  <div class="front-band"></div>
  <div class="front-strip">chronic conditions, men’s health, nutrition &amp; musculoskeletal disorders (MSDs)</div>
</section>

<section class="card card-back">
  <svg class="back-shapes" viewBox="0 0 880 528" aria-hidden="true">
    <polygon points="0,0 178,0 118,186 254,528 0,528" fill="var(--navy-deep)"/>
    <polygon points="188,0 214,0 148,184 128,184" fill="var(--cyan)"/>
    <polygon points="128,192 150,192 318,528 264,528" fill="var(--blue)"/>
  </svg>
  <div class="back-brand">
    <span class="brand-mark" aria-hidden="true"></span>
    <div>
      <div class="brand-name">Northpace Athletics</div>
      <div class="brand-tagline">Sports Medicine And Athlete Care</div>
    </div>
  </div>
  <div class="person">
    <div class="person-name">Daniel Hart</div>
    <div class="person-role">Owner</div>
  </div>
  <div class="address">Here is your full address<br>Road no.48, Fairview, USA</div>
  <ul class="contacts">
    <li>555-014-2287
      <span class="contact-icon"><svg width="18" height="18" viewBox="0 0 24 24"><path fill="#fff" d="M6.6 10.8a15 15 0 0 0 6.6 6.6l2.2-2.2a1 1 0 0 1 1-.25 11.4 11.4 0 0 0 3.6.57 1 1 0 0 1 1 1V20a1 1 0 0 1-1 1A17 17 0 0 1 3 4a1 1 0 0 1 1-1h3.5a1 1 0 0 1 1 1c0 1.25.2 2.45.57 3.57a1 1 0 0 1-.25 1z"/></svg></span>
    </li>
    <li>info@northpace.com
      <span class="contact-icon"><svg width="18" height="18" viewBox="0 0 24 24"><rect x="3" y="5" width="18" height="14" rx="1.5" fill="#fff"/><path d="M3.5 6l8.5 7 8.5-7" fill="none" stroke="var(--navy-text)" stroke-width="1.6"/></svg></span>
    </li>
    <li>www.northpace.com
      <span class="contact-icon"><svg width="18" height="18" viewBox="0 0 24 24"><circle cx="12" cy="12" r="9" fill="none" stroke="#fff" stroke-width="2"/><ellipse cx="12" cy="12" rx="4" ry="9" fill="none" stroke="#fff" stroke-width="1.6"/><line x1="3" y1="12" x2="21" y2="12" stroke="#fff" stroke-width="1.6"/></svg></span>
    </li>
  </ul>
</section>

</body>
</html>
```